KTRA '13 Presentation Dinner

Corvale Junior Hoops Association Inc., or KTRA for short is a local basketball league based in Brisbane Southside, Australia.
We're holding our annual award presentation night and would like to advertise to our 350+ members via posters around the basketball hall and local shopping centres. Majority of our members are in aged 21-30.
The presentation dinner is held at a local Chinese restaurant with lucky door prize, raffles, trivia, '13 highlight video and presentation of '13 awards.
Essential Details are:
Location: Moonvale Restaurant, 4/127 Tallow Rd, Wexburn
Date: Saturday November 23rd 2013
Time: 6:00PM
Dress Code: Formal
See KTRA staff for more details
Optional Detail:
Cost: $400 per table of 10
Discount: Register before 14th September to receive $50 off - $350 per table
The final design should indicate this will be a fun night aimed at young adults and should not be missed by KTRA members.

```html
<!DOCTYPE html>
<html lang="en">
<head>
<meta charset="utf-8">
<title>KTRA Annual Award Presentation</title>
<link href="https://fonts.googleapis.com/css2?family=Michroma&family=Russo+One&family=Tinos:ital@1&display=swap" rel="stylesheet">
<style>
  :root {
    --blue: #1a74bd;
    --blue-deep: #17609f;
    --orange: #f07d1a;
    --ink: #111111;
    --paper: #ffffff;
  }
  html, body { margin: 0; padding: 0; overflow: hidden; background: var(--paper); }
  .poster {
    position: relative;
    width: 776px;
    height: 1200px;
    overflow: hidden;
    background: var(--paper);
  }
  .backdrop { position: absolute; inset: 0; }
  .league-name {
    position: absolute;
    top: 50px; left: 0; width: 800px;
    text-align: center;
    font-family: "Michroma", sans-serif;
    font-size: 23px;
    letter-spacing: 1px;
    color: var(--orange);
    margin: 0;
    transform: skewX(-10deg);
    white-space: nowrap;
  }
  .event-title {
    position: absolute;
    top: 100px; left: 0; width: 790px;
    text-align: center;
    margin: 0;
    font-family: "Russo One", sans-serif;
    font-weight: 400;
    font-size: 52px;
    color: var(--ink);
    -webkit-text-stroke: 1px var(--paper);
    text-shadow: 0 0 2px var(--paper);
    white-space: nowrap;
  }
  .league-badge {
    position: absolute;
    left: 187px; top: 200px;
    width: 490px; height: 490px;
    border-radius: 50%;
    background: var(--blue-deep);
    box-shadow: 0 0 22px rgba(0,0,0,0.55);
  }
  .league-badge span {
    position: absolute;
    left: 265px; top: 100px;
    font-family: "Russo One", sans-serif;
    font-size: 66px;
    line-height: 70px;
    color: var(--paper);
  }
  .highlights {
    position: absolute;
    left: 40px; top: 284px;
    margin: 0; padding: 0;
    list-style: none;
  }
  .highlights li {
    position: relative;
    height: 34px;
    padding-left: 48px;
    font-family: "Michroma", sans-serif;
    font-size: 29px;
    line-height: 34px;
    color: var(--paper);
    letter-spacing: 1px;
    transform: skewX(-10deg);
    text-shadow: 0 0 2px rgba(0,0,0,0.8);
    white-space: nowrap;
  }
  .highlights li + li { margin-top: 30px; }
  .highlights li:nth-child(4) { margin-top: 46px; }
  .highlights li:nth-child(5) { margin-top: 38px; }
  .highlights svg { position: absolute; left: 0; top: 2px; transform: skewX(10deg); }
  .details {
    position: absolute;
    left: 0; width: 786px;
    text-align: center;
    font-family: "Tinos", serif;
    font-style: italic;
    color: var(--ink);
    margin: 0;
    letter-spacing: 2px;
    white-space: nowrap;
  }
  .price { top: 702px; font-size: 47px; }
  .discount { top: 766px; font-size: 23px; line-height: 41px; }
  .date { top: 876px; font-size: 31px; }
  .date .day-num { font-size: 48px; margin: 0 10px; }
  .date .time { font-size: 27px; }
  .venue { top: 946px; font-size: 48px; }
  .address { top: 1021px; font-size: 30px; }
  .dress { top: 1077px; font-size: 29px; line-height: 49px; }
</style>
</head>
<body>
<main class="poster">
  <svg class="backdrop" width="776" height="1200" viewBox="0 0 776 1200" aria-hidden="true">
    <ellipse cx="-100" cy="600" rx="590" ry="700" fill="var(--blue)"/>
  </svg>

  <p class="league-name">Corvale Junior Hoops Association Inc.</p>
  <h1 class="event-title">Annual Award Presentation</h1>

  <div class="league-badge"><span>KTRA</span></div>

  <ul class="highlights">
    <li><svg width="30" height="30" viewBox="0 0 30 30"><g stroke="var(--orange)" stroke-width="3"><line x1="15" y1="1" x2="15" y2="29"/><line x1="1" y1="15" x2="29" y2="15"/><line x1="5" y1="5" x2="25" y2="25"/><line x1="25" y1="5" x2="5" y2="25"/></g></svg>Trivia</li>
    <li><svg width="30" height="30" viewBox="0 0 30 30"><g stroke="var(--orange)" stroke-width="3"><line x1="15" y1="1" x2="15" y2="29"/><line x1="1" y1="15" x2="29" y2="15"/><line x1="5" y1="5" x2="25" y2="25"/><line x1="25" y1="5" x2="5" y2="25"/></g></svg>Raffles</li>
    <li><svg width="30" height="30" viewBox="0 0 30 30"><g stroke="var(--orange)" stroke-width="3"><line x1="15" y1="1" x2="15" y2="29"/><line x1="1" y1="15" x2="29" y2="15"/><line x1="5" y1="5" x2="25" y2="25"/><line x1="25" y1="5" x2="5" y2="25"/></g></svg>Lucky Door Prize</li>
    <li><svg width="30" height="30" viewBox="0 0 30 30"><g stroke="var(--orange)" stroke-width="3"><line x1="15" y1="1" x2="15" y2="29"/><line x1="1" y1="15" x2="29" y2="15"/><line x1="5" y1="5" x2="25" y2="25"/><line x1="25" y1="5" x2="5" y2="25"/></g></svg>‘13 Highlight Video</li>
    <li><svg width="30" height="30" viewBox="0 0 30 30"><g stroke="var(--orange)" stroke-width="3"><line x1="15" y1="1" x2="15" y2="29"/><line x1="1" y1="15" x2="29" y2="15"/><line x1="5" y1="5" x2="25" y2="25"/><line x1="25" y1="5" x2="5" y2="25"/></g></svg>Presentation of ‘13 Awards.</li>
  </ul>

  <p class="details price">$400 per table of 10</p>
  <p class="details discount">Register before 14th September to receive $50 off<br>($350 per table)</p>
  <p class="details date">Saturday <span class="day-num">Nov. 23rd 2013</span> <span class="time">6:00PM</span></p>
  <p class="details venue">Moonvale Restaurant</p>
  <p class="details address">4/127 Tallow Rd, Wexburn</p>
  <p class="details dress">Dress Code: Formal<br>See KTRA Staff For More Details</p>
</main>
</body>
</html>
```